New eyelid plastic surgery office needs a business card design-Eyelid Surgery Partners of Brennor

I recently used SketchHarbor for my logo design and was very pleased with creativity and results. It was a difficult decision for me. Now I would like to create a business card based on this logo, which I will attach.

The text should be easily legible as some of my patients have difficulty seeing, but I would like a subtle, sophisticated artistry also evident to make the card memorable. Would like the card based on a similar color scheme as the logo but the inverse or other complementary colors may prove interesting

A good question was asked...my concern about my visually impaired patients was really my desire to avoid italicized or calligraphic type fonts that may be hard to read. Standard font size for a business card would be fine. Thanks!

Thank you so much for the great work so far. I wanted to give you my particular contact information to see if that would change the look of the cards. Martin Pellowby, MD Address: 2817 Larkmoor Avenue, Suite 205 Wilmington, NC 28517 Phone: 910-555-0183 Fax: 910-555-0184 Website: www.brennorlidclinic.example Please delete the email slot from the card. Thanks so much!

Reason: Last minute consideration. So many great revisions right now!

Plastic

```html
<!DOCTYPE html>
<html lang="en">
<head>
<meta charset="utf-8">
<title>Eyelid Surgery Partners of Brennor – Business Card</title>
<link rel="stylesheet" href="https://fonts.googleapis.com/css2?family=Lato:wght@400;700&display=swap">
<style>
  :root {
    --stage: #e4e4e6;
    --card: #1b1b1d;
    --blue: #1459b5;
    --grey: #dcdcde;
    --ink: #ececec;
  }
  * { margin: 0; padding: 0; box-sizing: border-box; }
  html, body { width: 1200px; height: 1000px; overflow: hidden; }
  body {
    background: var(--stage);
    font-family: "Lato", Arial, sans-serif;
    position: relative;
  }
  .card {
    position: absolute;
    left: 100px; top: 215px;
    width: 1000px; height: 570px;
    background: var(--card);
    box-shadow: 0 12px 30px rgba(0,0,0,.35);
    overflow: hidden;
  }
  .brand-name {
    position: absolute;
    left: 60px; top: 62px;
    color: var(--blue);
    font-weight: 400;
    font-size: 44px;
    line-height: 1.12;
    letter-spacing: 1px;
    text-transform: uppercase;
  }
  .name-rule {
    position: absolute;
    left: 0; top: 242px;
    width: 545px; height: 6px;
    background: var(--blue);
  }
  .doctor {
    position: absolute;
    right: 170px; top: 200px;
    text-align: right;
  }
  .doctor-name {
    color: var(--blue);
    font-size: 31px;
    font-weight: 400;
    letter-spacing: .5px;
    text-transform: uppercase;
  }
  .doctor-credentials {
    color: var(--ink);
    font-size: 21px;
    margin-top: 2px;
  }
  .name-tick {
    position: absolute;
    left: 845px; top: 218px;
    width: 26px; height: 6px;
    background: var(--blue);
  }
  .name-tab {
    position: absolute;
    left: 882px; top: 203px;
    width: 118px; height: 36px;
    background: var(--grey);
  }
  .contact-list {
    position: absolute;
    left: 60px; top: 360px;
    list-style: none;
  }
  .contact-list li {
    display: flex;
    align-items: center;
    gap: 14px;
    color: var(--ink);
    font-size: 22px;
    height: 34px;
  }
  .contact-list svg { width: 22px; height: 22px; fill: var(--blue); flex: none; }
  .address {
    position: absolute;
    right: 60px; top: 325px;
    text-align: right;
    color: var(--ink);
    font-size: 22px;
    line-height: 1.45;
  }
  .address-title {
    color: var(--blue);
    text-transform: uppercase;
    letter-spacing: .5px;
  }
  .footer-bands {
    position: absolute;
    left: 0; bottom: 0;
    width: 1000px; height: 70px;
  }
</style>
</head>
<body>
  <div class="card">
    <div class="brand-name">Eyelid Surgery Partners<br>of Brennor</div>

    <div class="name-rule"></div>
    <div class="doctor">
      <div class="doctor-name">Graham Ellery</div>
      <div class="doctor-credentials">BSc - MBBS - M.D.</div>
    </div>
    <div class="name-tick"></div>
    <div class="name-tab"></div>

    <ul class="contact-list">
      <li>
        <svg viewBox="0 0 24 24" aria-hidden="true"><path d="M6.6 10.8a15 15 0 0 0 6.6 6.6l2.2-2.2a1 1 0 0 1 1-.25 11.4 11.4 0 0 0 3.6.57 1 1 0 0 1 1 1V20a1 1 0 0 1-1 1A17 17 0 0 1 3 4a1 1 0 0 1 1-1h3.5a1 1 0 0 1 1 1c0 1.25.2 2.45.57 3.57a1 1 0 0 1-.25 1z"/></svg>
        123 555 0199
      </li>
      <li>
        <svg viewBox="0 0 24 24" aria-hidden="true"><path d="M2 5h20v14H2zm2 2v.5l8 5 8-5V7zm0 2.8V17h16V9.8l-8 5z"/></svg>
        yourname@eyelidpartners.example
      </li>
      <li>
        <svg viewBox="0 0 24 24" aria-hidden="true"><path d="M12 2a10 10 0 1 0 0 20 10 10 0 0 0 0-20zm6.9 6h-3a15.6 15.6 0 0 0-1.4-3.6A8 8 0 0 1 18.9 8zM12 4c.8 1.2 1.5 2.5 1.9 4h-3.8c.4-1.5 1.1-2.8 1.9-4zM4.3 14a8 8 0 0 1 0-4h3.4a16 16 0 0 0 0 4zm.8 2h3a15.6 15.6 0 0 0 1.4 3.6A8 8 0 0 1 5.1 16zm3-8h-3a8 8 0 0 1 4.4-3.6C8.9 5.6 8.4 6.8 8.1 8zM12 20c-.8-1.2-1.5-2.5-1.9-4h3.8c-.4 1.5-1.1 2.8-1.9 4zm2.3-6H9.7a14.7 14.7 0 0 1 0-4h4.6a14.7 14.7 0 0 1 0 4zm.3 5.6c.6-1.1 1.1-2.3 1.4-3.6h3a8 8 0 0 1-4.4 3.6zm1.7-5.6a16 16 0 0 0 0-4h3.4a8 8 0 0 1 0 4z"/></svg>
        www.eyelidpartners.example
      </li>
    </ul>

    <address class="address" style="font-style:normal">
      <div class="address-title">Eyelid Surgery</div>
      <div>Suite 456, Marlow Road,</div>
      <div>Hartfield, US 54321</div>
    </address>

    <svg class="footer-bands" viewBox="0 0 1000 70" aria-hidden="true">
      <polygon points="0,42 612,42 604,62 0,62" fill="var(--blue)"/>
      <polygon points="628,28 1000,28 1000,46 620,46" fill="var(--grey)"/>
    </svg>
  </div>
</body>
</html>
```